Flyer-Design für Immobilienhändler
Zielgruppe
Ich bin ein kleiner Immobilienhändler (nebenberuflich, meine Frau und ich, 2-Mann Unternehmen) und kaufe direkt Wohnimmobilen (Haus/Wohnungen) ein, um diese aufzuwerten und dann wieder zu verkaufen. Ich bin kein Makler, habe aber ähnliche Zielgruppen wie ein Makler, nur mit dem Unterschied das ich die Immos direkt kostenfrei kaufe so wie sie sind! Zielgruppe sind bei mir Privatpersonen (im mittlerem-höherem Alter 50-80 Jahre) die Ihre Immobilie verkaufen möchten.
Aufgabenstellung
Es soll ein Flyer sein mit folgenden Vorgaben:
• Design: Modern, einfach und wichtig ist das es professional und sehr seriös wirkt
• Auf den ersten Blick sollte die Message verständlich sein was ich suche und was die Vorteile sind es bei mir zu verkaufen, anstatt das einem Makler zu übergeben (siehe mein Entwurf).
• Flyer Format z.B. DIN A5/A6, was sich gut versenden lässt. Vorschläge sind willkommen
Im Anhang habe ein einen eigenen Entwurf beigefügt, jedoch bin offen für komplett neue Vorschläge was Text und Design angeht.

```html
<!DOCTYPE html>
<html lang="de">
<head>
<meta charset="utf-8">
<title>Wohnwerk Flyer</title>
<link href="https://fonts.googleapis.com/css2?family=Montserrat:wght@400;500;600;700;800&display=swap" rel="stylesheet">
<style>
  :root {
    --blue: #1b4e94;
    --yellow: #f9b800;
    --paper: #ffffff;
    --stage: #ececec;
    --art-light: #e3ebf6;
    --art-mid: #c4d3ea;
  }
  * { box-sizing: border-box; margin: 0; padding: 0; }
  html, body { width: 1200px; height: 2890px; overflow: hidden; }
  body {
    background: var(--stage);
    font-family: 'Montserrat', sans-serif;
    color: var(--blue);
    position: relative;
  }
  .flyer {
    position: absolute;
    left: 62px;
    width: 1076px;
    height: 757px;
    background: var(--paper);
    box-shadow: 0 6px 18px rgba(0,0,0,0.18);
    overflow: hidden;
  }
  .flyer--front { top: 658px; }
  .flyer--back { top: 1475px; }

  .bar { position: absolute; }
  .bar--blue { background: var(--blue); }
  .bar--yellow { background: var(--yellow); }

  .brand {
    position: absolute;
    display: flex;
    align-items: center;
    gap: 12px;
    font-weight: 600;
    font-size: 26px;
    letter-spacing: 6px;
    color: var(--blue);
  }
  .brand__square {
    width: 22px; height: 22px;
    background: var(--yellow);
  }

  .front__headline {
    position: absolute;
    left: 85px; top: 235px;
    font-weight: 800;
    font-size: 51px;
    line-height: 61px;
  }
  .front__sub {
    position: absolute;
    left: 85px; top: 386px;
    font-weight: 500;
    font-size: 31px;
    line-height: 37px;
    color: var(--yellow);
  }
  .skyline {
    position: absolute;
    background: linear-gradient(180deg, var(--art-light), var(--art-mid));
  }

  .back__title {
    position: absolute;
    left: 78px; top: 108px;
    font-weight: 800;
    font-size: 53px;
  }
  .col-heading {
    font-weight: 700;
    font-size: 21px;
    margin-bottom: 10px;
  }
  .about {
    position: absolute;
    left: 78px; top: 210px;
    width: 400px;
  }
  .about p {
    font-size: 17px;
    line-height: 21px;
  }
  .about .signature {
    margin-top: 24px;
    font-weight: 700;
  }
  .reasons {
    position: absolute;
    left: 590px; top: 210px;
    width: 440px;
  }
  .reasons ul { list-style: none; }
  .reasons li {
    position: relative;
    font-size: 17px;
    line-height: 21px;
    margin-bottom: 22px;
  }
  .reasons li svg {
    position: absolute;
    left: -36px; top: 3px;
  }
  .contact {
    position: absolute;
    right: 56px; top: 600px;
    text-align: right;
  }
  .contact__ask {
    font-weight: 700;
    font-size: 21px;
    line-height: 26px;
    margin-bottom: 8px;
  }
  .contact__line {
    display: flex;
    justify-content: flex-end;
    align-items: center;
    gap: 14px;
    font-size: 17px;
    line-height: 25px;
  }
</style>
</head>
<body>

<section class="flyer flyer--front">
  <div class="bar bar--blue" style="left:665px; top:0; width:411px; height:18px;"></div>
  <div class="brand" style="left:85px; top:82px;"><span class="brand__square"></span>WOHNWERK</div>
  <h1 class="front__headline">Sie möchten Ihre Immobilie<br>zum Bestpreis verkaufen?</h1>
  <p class="front__sub">Ohne Renovierung/Sanierung<br>Ohne Gebühren und Besucherstress</p>
  <div class="bar bar--yellow" style="left:0; top:565px; width:18px; height:192px;"></div>
  <div class="skyline" role="img" aria-label="Linienillustration einer Stadtsilhouette mit Häusern, Kirche, Bäumen und Fabrik" style="left:20px; top:525px; width:1040px; height:232px;"></div>
</section>

<section class="flyer flyer--back">
  <div class="bar bar--blue" style="left:0; top:0; width:410px; height:16px;"></div>
  <div class="bar bar--yellow" style="left:1058px; top:0; width:18px; height:195px;"></div>
  <h2 class="back__title">Wir kaufen Ihre Immobilie</h2>

  <div class="about">
    <h3 class="col-heading">Wer sind wir?</h3>
    <p>Wir sind keine Makler. Wi sind kein Familienunternehme das sich auf den Immobilien ankauf im Rhein-Main Gebit spezialisiert hat. Wir kaufe gute und solide Immobilienz um Bestpreis, direkt.</p>
    <p class="signature">Dipl.-Bauing. Markus Lindner</p>
  </div>
  <div class="brand" style="left:78px; top:435px; font-size:22px; letter-spacing:5px;"><span class="brand__square" style="width:18px;height:18px;"></span>WOHNWERK</div>

  <div class="reasons">
    <h3 class="col-heading">Warum mit uns?</h3>
    <ul>
      <li><svg width="16" height="14" viewBox="0 0 16 14"><path d="M2 7l4 4 8-9" fill="none" stroke="#f9b800" stroke-width="2"/></svg>Abkauf direkt von uns, zum fairen Bestpreis</li>
      <li><svg width="16" height="14" viewBox="0 0 16 14"><path d="M2 7l4 4 8-9" fill="none" stroke="#f9b800" stroke-width="2"/></svg>Professionelle, schnelle und komplette<br>Kaufabwicklung aus einer Hand</li>
      <li><svg width="16" height="14" viewBox="0 0 16 14"><path d="M2 7l4 4 8-9" fill="none" stroke="#f9b800" stroke-width="2"/></svg>Sie brauchen nicht renovieren, sanieren oder<br>entrümpeln</li>
      <li><svg width="16" height="14" viewBox="0 0 16 14"><path d="M2 7l4 4 8-9" fill="none" stroke="#f9b800" stroke-width="2"/></svg>Keine Maklergebühr, kein Besucherstress</li>
      <li><svg width="16" height="14" viewBox="0 0 16 14"><path d="M2 7l4 4 8-9" fill="none" stroke="#f9b800" stroke-width="2"/></svg>Kein Haftungsrisiko -Wir kaufen Ihre<br>Immobilie so wie sie ist</li>
    </ul>
  </div>

  <div class="skyline" role="img" aria-label="Linienillustration von Stadthäusern und einer Kirche" style="left:15px; top:475px; width:480px; height:282px;"></div>

  <div class="contact">
    <p class="contact__ask">Sie möchten ein<br>unverbindliches Angebot?</p>
    <p class="contact__line">ml@wohnwerk-haus.de
      <svg width="16" height="12" viewBox="0 0 16 12"><rect width="16" height="12" fill="#f9b800"/><path d="M0 0l8 6 8-6" fill="none" stroke="#fff" stroke-width="1.5"/></svg>
    </p>
    <p class="contact__line">06021 / 45 78 31
      <svg width="16" height="16" viewBox="0 0 16 16"><path d="M3 1l3 0 1 4-2 1c1 2 3 4 5 5l1-2 4 1 0 3c0 1-1 2-2 2C7 15 1 9 1 3c0-1 1-2 2-2z" fill="#f9b800"/></svg>
    </p>
  </div>
</section>

</body>
</html>
```